We need a logo design that explain all the products we possess.
The main goal is to represent graphically all the logos, pointing to one single logo - Voltane.
The descriptions are in french.
I have uploaded a file with 4 logos to use:
Voltane (the logo that all the rest should be pointing to)
RDM
Parcelin
PattouMou
All logo must be used in the vector graphic format, the description file is in each folder, it's the description that should be next to the logo.

The main goal of this is to create a banner 10' x 11' (estimated)

Target Market(s)

Cities

Requirements
Must have
• All the logos in the zip file in vector graphic.
Nice to have
• A background
Should not have
• Do not use TOB logo, it's a mix with RDM, and Tob Blue/dark blue with inscription "RDM", Charging fees for a part of the picture is not ok!

```html
<!DOCTYPE html>
<html lang="fr">
<head>
<meta charset="utf-8">
<title>Portail Voltane 2.0 – Bannière</title>
<link href="https://fonts.googleapis.com/css2?family=Montserrat:wght@500;600;700;800&display=swap" rel="stylesheet">
<style>
  :root {
    --page-bg: #e4e4e4;
    --banner-bg: #ffffff;
    --banner-shade: #eceef0;
    --coral: #e8705e;
    --brand-blue: #2f7fc1;
    --text-grey: #555b61;
    --ring-grey: #c9ced3;
    --green: #8cc63f;
    --teal: #4b8c9c;
    --sky-blue: #1b9ad6;
    --dash: #7aa7c9;
    --city-dark: #9aa1a8;
    --city-light: #e6e8eb;
  }
  * { margin: 0; padding: 0; box-sizing: border-box; }
  html, body { width: 779px; height: 1200px; overflow: hidden; }
  body {
    background: var(--page-bg);
    font-family: "Montserrat", Arial, sans-serif;
    display: flex; align-items: center; justify-content: center;
  }
  .banner {
    position: relative;
    width: 640px; height: 600px;
    background: radial-gradient(ellipse at 50% 45%, var(--banner-bg) 40%, var(--banner-shade) 100%);
    overflow: hidden;
    box-shadow: 0 6px 18px rgba(0,0,0,.18);
  }
  .banner__art { position: absolute; inset: 0; }
  .hub {
    position: absolute; left: 210px; top: 40px;
    width: 220px; height: 220px; border-radius: 50%;
    background: var(--banner-bg);
    border: 8px solid var(--ring-grey);
    box-shadow: 0 4px 12px rgba(0,0,0,.2);
    display: flex; flex-direction: column; align-items: center; justify-content: center;
  }
  .hub__brand {
    display: flex; align-items: center; gap: 8px;
    color: var(--brand-blue); font-weight: 800; font-size: 28px; letter-spacing: 1px;
  }
  .hub__dot { width: 14px; height: 14px; border-radius: 50%; background: var(--brand-blue); }
  .hub__tagline {
    margin-top: 10px; text-align: center;
    color: var(--text-grey); font-weight: 600; font-size: 13px; line-height: 1.3; letter-spacing: .5px;
  }
  .service {
    position: absolute; width: 200px;
    display: flex; flex-direction: column; align-items: center;
  }
  .service__badge {
    width: 136px; height: 136px; border-radius: 50%;
    background: var(--banner-bg);
    border: 9px solid var(--ring);
    box-shadow: 0 3px 10px rgba(0,0,0,.18);
    display: flex; align-items: center; justify-content: center;
  }
  .service__name { color: var(--ring); font-weight: 700; font-size: 18px; }
  .service__label {
    margin-top: 12px; text-align: center;
    color: var(--text-grey); font-weight: 700; font-size: 14px; line-height: 1.3;
  }
  .service--paperless { --ring: var(--green); left: 20px; top: 290px; }
  .service--land { --ring: var(--teal); left: 220px; top: 330px; }
  .service--pets { --ring: var(--sky-blue); left: 420px; top: 290px; }
  .service--land .service__badge { width: 146px; height: 146px; }
  .city-band {
    position: absolute; bottom: 0; width: 200px; height: 56px;
    background: linear-gradient(to top, var(--city-dark) 0%, var(--city-light) 100%);
  }
  .city-band--left { left: 0; }
  .city-band--right { right: 0; }
  .banner__url {
    position: absolute; bottom: 14px; left: 0; right: 0; text-align: center;
    color: var(--text-grey); font-weight: 700; font-size: 14px; letter-spacing: 1px;
  }
</style>
</head>
<body>
  <main class="banner">
    <svg class="banner__art" width="640" height="600" viewBox="0 0 640 600" aria-hidden="true">
      <defs>
        <marker id="arrow-head" viewBox="0 0 10 10" refX="6" refY="5" markerWidth="6" markerHeight="6" orient="auto">
          <path d="M0 0 L10 5 L0 10 z" fill="var(--dash)"/>
        </marker>
      </defs>
      <ellipse class="top-band" cx="320" cy="0" rx="360" ry="120" fill="var(--coral)"/>
      <path d="M240 240 Q150 250 120 290" fill="none" stroke="var(--dash)" stroke-width="3" stroke-dasharray="8 6" marker-end="url(#arrow-head)"/>
      <path d="M400 240 Q490 250 520 290" fill="none" stroke="var(--dash)" stroke-width="3" stroke-dasharray="8 6" marker-end="url(#arrow-head)"/>
      <path d="M320 268 L320 326" fill="none" stroke="var(--dash)" stroke-width="3" stroke-dasharray="8 6" marker-end="url(#arrow-head)"/>
    </svg>

    <section class="hub">
      <div class="hub__brand"><span class="hub__dot"></span>VOLTANE</div>
      <p class="hub__tagline">PORTAIL<br>VOLTANE 2.0</p>
    </section>

    <section class="service service--paperless">
      <div class="service__badge"><span class="service__name">RDM</span></div>
      <p class="service__label">CONSEIL<br>SANS PAPIER</p>
    </section>

    <section class="service service--land">
      <div class="service__badge"><span class="service__name">PARCELIN</span></div>
      <p class="service__label">PERMIS | CARTE<br>INVENTAIRE | TAXES</p>
    </section>

    <section class="service service--pets">
      <div class="service__badge"><span class="service__name">PattouMou</span></div>
      <p class="service__label">LICENCES<br>POUR ANIMAUX</p>
    </section>

    <div class="city-band city-band--left" role="img" aria-label="Illustration de ville en gris"></div>
    <div class="city-band city-band--right" role="img" aria-label="Illustration de ville en gris"></div>
    <p class="banner__url">www.voltaneportail.com</p>
  </main>
</body>
</html>
```